Business Card

We need some ideas for corporate business cards. I'm interested in a double sided card, with one side featuring our corporate logo, the other side with employee information.

Corporate colors, logo etc. available at www.brivalo.com

Industry/Entity Type

Business

Requirements
Must have
• The "Brivalo" logo with stylized "O"

Nice to have
• Preferred font is calibri

```html
<!DOCTYPE html>
<html lang="en">
<head>
<meta charset="utf-8">
<title>Brivalo Business Card</title>
<link href="https://fonts.googleapis.com/css2?family=Carlito:wght@400;700&display=swap" rel="stylesheet">
<style>
  :root {
    --page: #e9efee;
    --sky: #5cbffa;
    --orange: #f98a1d;
    --white: #ffffff;
    --name-blue: #2f6fbd;
    --title-brown: #b4520c;
    --contact-blue: #2b5c9f;
    --label-cream: #fdf0df;
  }
  * { margin: 0; padding: 0; box-sizing: border-box; }
  html, body {
    width: 1011px; height: 1200px; overflow: hidden;
    background: var(--page);
    font-family: "Carlito", "Calibri", sans-serif;
  }
  .canvas { position: relative; width: 1011px; height: 1200px; }

  .card { position: absolute; width: 767px; height: 444px; overflow: hidden; }
  .card--front { left: 118px; top: 109px; background: var(--white); }
  .card--back { left: 126px; top: 662px; background: var(--sky); }

  .front-band {
    position: absolute; left: 0; top: 0; width: 100%; height: 204px;
    background: var(--sky); border-bottom: 7px solid var(--orange);
  }
  .wordmark {
    position: absolute; color: var(--white); font-weight: 700;
    letter-spacing: 0.08em; line-height: 1;
  }
  .front-band .wordmark { left: 50px; top: 62px; font-size: 28px; }

  .employee { position: absolute; left: 0; top: 213px; width: 100%; text-align: center; }
  .employee__name { font-size: 33px; color: var(--name-blue); line-height: 1.1; }
  .employee__title { font-size: 25px; font-weight: 700; color: var(--title-brown); margin-top: 6px; }

  .contact {
    position: absolute; font-size: 21px; font-weight: 700;
    color: var(--contact-blue); line-height: 30px;
  }
  .contact--phones { left: 77px; top: 352px; }
  .contact--address { right: 37px; top: 322px; text-align: right; }

  .card--back .wordmark {
    left: 0; top: 158px; width: 100%; text-align: center;
    font-size: 56px; font-weight: 400; letter-spacing: 0.16em;
  }
  .values { position: absolute; left: 0; top: 250px; width: 100%; }
  .value { position: absolute; width: 200px; text-align: center; }
  .value:nth-child(1) { left: 41px; }
  .value:nth-child(2) { left: 291px; }
  .value:nth-child(3) { left: 542px; }
  .value__label { font-size: 21px; color: var(--label-cream); line-height: 1; }
  .value__icon { display: block; margin: 12px auto 0; width: 56px; height: 56px; }
</style>
</head>
<body>
<div class="canvas">

  <section class="card card--front">
    <div class="front-band">
      <div class="wordmark">BRIVALO</div>
    </div>
    <div class="employee">
      <div class="employee__name">John Doe</div>
      <div class="employee__title">Senior Software Engineer</div>
    </div>
    <div class="contact contact--phones">
      <div>Tel:&nbsp; +1 555 014 7731</div>
      <div>Fax: +1 555 014 2290</div>
    </div>
    <div class="contact contact--address">
      <div>2450 Harbor Point Drive</div>
      <div>Suite 410</div>
      <div>Easton, 20145, VA</div>
    </div>
  </section>

  <section class="card card--back">
    <div class="wordmark">BRIVALO</div>
    <div class="values">
      <div class="value">
        <div class="value__label">Technology</div>
        <svg class="value__icon" viewBox="0 0 56 56" aria-hidden="true">
          <g fill="var(--orange)" transform="translate(28 28)">
            <rect x="-5" y="-24" width="10" height="10" rx="2"/>
            <rect x="-5" y="-24" width="10" height="10" rx="2" transform="rotate(45)"/>
            <rect x="-5" y="-24" width="10" height="10" rx="2" transform="rotate(90)"/>
            <rect x="-5" y="-24" width="10" height="10" rx="2" transform="rotate(135)"/>
            <rect x="-5" y="-24" width="10" height="10" rx="2" transform="rotate(180)"/>
            <rect x="-5" y="-24" width="10" height="10" rx="2" transform="rotate(225)"/>
            <rect x="-5" y="-24" width="10" height="10" rx="2" transform="rotate(270)"/>
            <rect x="-5" y="-24" width="10" height="10" rx="2" transform="rotate(315)"/>
            <circle r="17"/>
            <circle r="7" fill="var(--sky)"/>
          </g>
        </svg>
      </div>
      <div class="value">
        <div class="value__label">Solutions</div>
        <svg class="value__icon" viewBox="0 0 56 56" aria-hidden="true">
          <circle cx="28" cy="28" r="24" fill="none" stroke="var(--orange)" stroke-width="4"/>
          <circle cx="28" cy="28" r="16" fill="var(--orange)"/>
          <path d="M36 20 L30 30 L26 26 Z" fill="var(--sky)"/>
          <path d="M20 36 L26 26 L30 30 Z" fill="var(--sky)" opacity="0.55"/>
        </svg>
      </div>
      <div class="value">
        <div class="value__label">Vision</div>
        <svg class="value__icon" viewBox="0 0 56 56" aria-hidden="true">
          <path d="M3 28 Q28 4 53 28 Q28 52 3 28 Z" fill="var(--orange)"/>
          <circle cx="28" cy="28" r="11" fill="var(--sky)"/>
          <circle cx="28" cy="28" r="6" fill="var(--orange)"/>
          <circle cx="25" cy="25" r="2.5" fill="var(--sky)"/>
        </svg>
      </div>
    </div>
  </section>

</div>
</body>
</html>
```